The Timber Loft

We need a business card design for our wardrobe company.
Please visit our website www.zorvelcabinets.com to get an idea of who we are.

```html
<!DOCTYPE html>
<html lang="en">
<head>
<meta charset="utf-8">
<title>The Timber Loft – Business Card</title>
<link rel="stylesheet" href="https://fonts.googleapis.com/css2?family=Arimo:wght@700&family=Lato:wght@400&family=Open+Sans:wght@400;700&display=swap">
<style>
  :root {
    --stage: #e4e4e4;
    --card: #ffffff;
    --gold: #8d7450;
    --ink: #1e1e1e;
    --text: #3f3f3f;
    --rule: #b29d78;
  }
  * { margin: 0; padding: 0; box-sizing: border-box; }
  html, body { width: 1200px; height: 1200px; overflow: hidden; }
  body {
    background: var(--stage);
    position: relative;
  }
  .business-card {
    position: absolute;
    left: 60px;
    top: 286px;
    width: 1080px;
    height: 628px;
    background: var(--card);
  }
  .brand-mark {
    position: absolute;
    left: 45px;
    top: 88px;
    width: 40px;
    height: 40px;
    background: var(--gold);
  }
  .brand-text {
    position: absolute;
    left: 221px;
    top: 78px;
    font-family: "Open Sans", sans-serif;
    font-weight: 700;
    color: var(--ink);
  }
  .brand-name { font-size: 26px; letter-spacing: 0.5px; line-height: 34px; }
  .brand-tagline { font-size: 20px; line-height: 34px; padding-left: 27px; }

  .holder-name {
    position: absolute;
    right: 50px;
    top: 322px;
    font-family: "Arimo", sans-serif;
    font-weight: 700;
    font-size: 39px;
    color: var(--gold);
  }
  .divider {
    position: absolute;
    left: 45px;
    top: 397px;
    width: 822px;
    height: 2px;
    background: var(--rule);
  }
  .holder-role {
    position: absolute;
    right: 50px;
    top: 377px;
    font-family: "Open Sans", sans-serif;
    font-size: 32px;
    line-height: 42px;
    color: var(--text);
  }
  .contact-list {
    position: absolute;
    left: 45px;
    top: 456px;
    list-style: none;
    font-family: "Lato", sans-serif;
    font-size: 26px;
    color: var(--text);
  }
  .contact-list li {
    display: flex;
    align-items: center;
    height: 33.5px;
    gap: 10px;
  }
  .contact-icon { width: 16px; height: 16px; fill: var(--gold); flex: none; }
  .address {
    position: absolute;
    right: 50px;
    top: 523px;
    font-family: "Lato", sans-serif;
    font-size: 26px;
    line-height: 33.5px;
    color: var(--text);
    text-align: right;
    font-style: normal;
  }
</style>
</head>
<body>
  <section class="business-card">
    <span class="brand-mark"></span>
    <header class="brand-text">
      <div class="brand-name">THE TIMBER LOFT</div>
      <div class="brand-tagline">Built Right, Fitted True</div>
    </header>

    <h1 class="holder-name">Dara Holcombe</h1>
    <div class="divider"></div>
    <p class="holder-role">Manager</p>

    <ul class="contact-list">
      <li>
        <svg class="contact-icon" viewBox="0 0 16 16" aria-hidden="true"><path d="M3.5 1.5l2.5 0 1 3.5-1.8 1.2a8 8 0 0 0 4.6 4.6L11 9l3.5 1v2.5c0 1-1 2-2 2C6.5 14.5 1.5 9.5 1.5 3.5c0-1 1-2 2-2z"/></svg>
        403-555-0142
      </li>
      <li>
        <svg class="contact-icon" viewBox="0 0 16 16" aria-hidden="true"><path d="M4.5 1h7a1 1 0 0 1 1 1v12a1 1 0 0 1-1 1h-7a1 1 0 0 1-1-1V2a1 1 0 0 1 1-1zm.5 2v9h6V3z"/></svg>
        403-555-0187
      </li>
      <li>
        <svg class="contact-icon" viewBox="0 0 16 16" aria-hidden="true"><path d="M1 3h14v10H1zm1.5 1.5v.4L8 8.6l5.5-3.7v-.4z"/></svg>
        info@zorvelcabinets.com
      </li>
      <li>
        <svg class="contact-icon" viewBox="0 0 16 16" aria-hidden="true"><path d="M8 1a7 7 0 1 0 0 14A7 7 0 0 0 8 1zm-1 2.2v2L5 7 3.3 6.2A5 5 0 0 1 7 3.2zm2 9.6V11l2-2 1.8.6A5 5 0 0 1 9 12.8z"/></svg>
        www.zorvelcabinets.com
      </li>
    </ul>

    <address class="address">
      18-20 Marlow Brenning<br>
      Street 552190, USA
    </address>
  </section>
</body>
</html>
```